Corvell Tarn manufacturing Project

We are looking at getting a brand new design for a new company that deals in selling stainless tubing and other stainless still products such as handrails, Spigots, Balustrade Fittings
Glass, Glass fittings and Aluminium Channels

We require a very clean website that deals with the following colours:

Blue to light blues
Blacks
Greys to light Greys
Whites

We are open for other ideas BUT we *DO NOT* want any pinks, greens or bright colours except for backgrounds colours we have chosen above. (It can be solid, gradient or a subtle pattern)

YOU MUST KEEP THE LOGO AS IS. PLEASE DO NOT ALTER THE LOGO IN *ANY WAY* and the logo MUST be the same colours and fonts.

Logo is attached.

The site must contain these aspects:
jQuery Slider (Image slide show)
Top drop down Menus
Be no more than 900px wide
Text is to be to the k9R standards. (no special fonts)

We will chop up the design into html format. You just need to provide the PSD file.

The clients opposition is:
www.polbrenwick.com

It Company

• Alter the logo in anyway

```html
<!DOCTYPE html>
<html lang="en">
<head>
<meta charset="utf-8">
<title>Corvell Tarn Metal</title>
<link rel="stylesheet" href="https://fonts.googleapis.com/css2?family=Noto+Sans:ital,wght@0,400;0,700;1,400;1,700&display=swap">
<style>
:root{
  --navy:#2c4f80;
  --blue:#1d4d8c;
  --ink:#222;
  --text:#333;
  --muted:#555;
  --bg:#e3e3e3;
  --frame:#fff;
  --field:#e9e9e9;
  --field-edge:#c4c4c4;
  --dark:#333;
}
*{box-sizing:border-box;margin:0;padding:0}
html,body{width:977px;height:1200px;overflow:hidden}
body{position:relative;font-family:"Noto Sans",Arial,sans-serif;color:var(--text);
  background:radial-gradient(ellipse 520px 420px at 260px 120px,#fafafa 0%,rgba(250,250,250,0) 100%),var(--bg)}
.abs{position:absolute}
.top-bar{left:0;top:0;width:977px;height:7px;background:var(--navy)}
.brand{left:88px;top:20px;width:140px;text-align:center}
.brand-mark{width:88px;height:88px;margin:0 auto;border-radius:50%;background:#2c2c2c;border:4px solid #b9c2cc}
.brand-name{margin-top:8px;font-size:15px;color:var(--ink);white-space:nowrap}
.brand-sub{font-size:7px;letter-spacing:1.5px;color:var(--ink);white-space:nowrap}
.search{left:714px;top:21px;width:180px;height:30px;border-radius:15px;border:1px solid #c9c9c9;
  background:linear-gradient(#dedede,#f4f4f4);box-shadow:inset 0 1px 2px rgba(0,0,0,.15)}
.search svg{position:absolute;left:9px;top:7px}
.main-nav{left:410px;top:115px;width:487px;height:27px;display:flex;justify-content:space-between;align-items:center;font-size:11.5px;color:var(--ink)}
.main-nav span{padding:0 0}
.main-nav .active{background:var(--navy);color:#fff;width:63px;height:27px;line-height:27px;text-align:center}
.slide{background:var(--frame);padding:5px;box-shadow:0 10px 12px -8px rgba(0,0,0,.35)}
.slide div{width:100%;height:100%}
.slide-left{left:122px;top:203px;width:175px;height:193px}
.slide-left div{background:linear-gradient(135deg,#c7cbcf,#8b5a2e 60%,#6e3f1c)}
.slide-right{left:674px;top:203px;width:179px;height:197px}
.slide-right div{background:linear-gradient(135deg,#e8e8e6,#d8d8d6 50%,#b9b9b7)}
.slide-main{left:291px;top:174px;width:387px;height:260px;z-index:2}
.slide-main div{background:linear-gradient(135deg,#b7bfc4,#b37a46 45%,#caa780 70%,#9a5a32)}
.slide-arrow{width:34px;height:34px}
.intro-title{left:0;top:476px;width:977px;display:flex;justify-content:center;align-items:center;gap:8px}
.intro-title .dot{width:41px;height:41px;border-radius:50%;background:#2c2c2c;border:3px solid #b9c2cc}
.intro-title h1{font-weight:400;font-size:28px;color:var(--ink)}
.intro-title h1 b{font-weight:400;color:var(--blue)}
.intro{left:98px;top:533px;width:783px;text-align:center;font-size:8.6px;line-height:14.6px;color:var(--text)}
.intro strong{font-style:italic;color:var(--ink)}
.intro p+p{margin-top:14.6px}
.rule{left:90px;width:797px;height:2px;background:linear-gradient(90deg,rgba(180,180,180,0),#c4c4c4 50%,rgba(180,180,180,0))}
.col{top:672px;width:200px}
.col h2{font-size:19px;color:var(--blue);font-weight:700;letter-spacing:.3px;line-height:22px}
.col h3{font-size:11px;color:var(--muted);font-weight:700;margin-left:1px;line-height:14px}
.col .pic{width:198px;height:105px;background:var(--frame);padding:5px;margin:10px 0 0 -4px;box-shadow:0 1px 3px rgba(0,0,0,.2)}
.col .pic div{width:100%;height:100%}
.col p{font-size:9px;line-height:14.6px;text-align:justify;margin:15px 0 0 -3px;width:199px}
.col-divider{top:674px;height:225px;border-left:1px dotted #aaa}
.section-title{font-size:19px;color:var(--blue);font-weight:700;letter-spacing:.3px}
.field{left:98px;width:188px;border:1px solid var(--field-edge);border-radius:5px;background:var(--field);
  box-shadow:inset 0 1px 2px rgba(0,0,0,.12);font-size:9px;color:#555;padding:0 9px}
.submit{left:222px;top:1098px;width:61px;height:20px;background:var(--dark);color:#fff;font-size:10px;font-weight:700;text-align:center;line-height:20px}
.vline{left:341px;top:947px;height:170px;border-left:1px solid #d0d0d0}
.products{left:381px;top:967px;width:457px;height:129px;border-radius:10px;background:#f4f4f4;box-shadow:0 2px 4px rgba(0,0,0,.18)}
.thumb{top:987px;height:96px;background:var(--frame);padding:3px;box-shadow:0 1px 3px rgba(0,0,0,.2)}
.thumb div{width:100%;height:100%}
.footer{left:0;top:1153px;width:977px;height:47px;background:var(--navy);color:#fff;text-align:center}
.footer nav{font-size:9.5px;padding-top:10px;word-spacing:0}
.footer nav span{margin:0 8px}
.footer p{font-size:9.5px;margin-top:5px}
</style>
</head>
<body>
<div class="abs top-bar"></div>

<header>
  <div class="abs brand">
    <div class="brand-mark"></div>
    <div class="brand-name">Corvell Tarn Metal</div>
    <div class="brand-sub">Manufacturing Co. Ltd</div>
  </div>
  <div class="abs search">
    <svg width="16" height="16" viewBox="0 0 16 16"><circle cx="6" cy="6" r="4.5" fill="none" stroke="#333" stroke-width="1.6"/><line x1="9.5" y1="9.5" x2="14" y2="14" stroke="#333" stroke-width="2.2"/></svg>
  </div>
  <nav class="abs main-nav">
    <span class="active">Home</span><span>About</span><span>Qingdao</span><span>Products</span><span>Download</span><span>Contact us</span>
  </nav>
</header>

<section class="slider">
  <svg class="abs slide-arrow" style="left:82px;top:284px" viewBox="0 0 34 34"><circle cx="17" cy="17" r="15" fill="#f0f0f0" stroke="#b5b5b5" stroke-width="2"/><path d="M20 10 L12 17 L20 24Z" fill="#aaa"/></svg>
  <div class="abs slide slide-left"><div role="img" aria-label="Glass balustrade on timber staircase"></div></div>
  <div class="abs slide slide-right"><div role="img" aria-label="White staircase with stainless rod railing"></div></div>
  <div class="abs slide slide-main"><div role="img" aria-label="Curved glass balustrade with stainless handrail on stairs"></div></div>
  <svg class="abs slide-arrow" style="left:859px;top:284px" viewBox="0 0 34 34"><circle cx="17" cy="17" r="15" fill="#f0f0f0" stroke="#b5b5b5" stroke-width="2"/><path d="M14 10 L22 17 L14 24Z" fill="#aaa"/></svg>
</section>

<section>
  <div class="abs intro-title"><div class="dot"></div><h1>Corvell Tarn <b>Metal</b></h1></div>
  <div class="abs intro">
    <p><strong>Lorem Ipsum has been the industry's standard dummy text ever since the 1500s, when an unknown printer took a galley of type and scrambled it to make a type specimen book. industry's standard dummy text ever since the 1500s,</strong> when an unknown printer took a galley of type and scrambled it to make a type specimen book. industry's standard dummy text ever since the 1500s, when an unknown printer took a galley of type and scrambled it to make a type specimen book.</p>
    <p>It has survived not only five centuries, but also the leap into electronic typesetting, remaining essentially unchanged. It was popularised in the 1960s with the release of Letraset sheets containing Lorem Ipsum passages, and more recently with desktop publishing software like Aldus PageMaker including versions of Lorem Ipsum.</p>
  </div>
</section>

<div class="abs rule" style="top:646px"></div>

<section>
  <article class="abs col" style="left:114px">
    <h2>Overview</h2><h3>our company profile</h3>
    <div class="pic"><div role="img" aria-label="Staircase with timber handrail and white balusters" style="background:linear-gradient(135deg,#8e4f2a,#c8c6bd 45%,#8a8a6a)"></div></div>
    <p>Aliquam eleifend lacus ac tellus volutpat porttitor. Suspendisse imperdiet tortor ut tortor bibendum pulvinar...</p>
  </article>
  <div class="abs col-divider" style="left:338px"></div>
  <article class="abs col" style="left:375px">
    <h2>Features</h2><h3>Solution Complete glass</h3>
    <div class="pic"><div role="img" aria-label="Glass balcony railing overlooking the sea" style="background:linear-gradient(#bcd3e6,#6d8aa3 45%,#d6d6d6 80%)"></div></div>
    <p>Aliquam eleifend lacus ac tellus volutpat porttitor. Suspendisse imperdiet tortor ut tortor bibendum pulvinar...</p>
  </article>
  <div class="abs col-divider" style="left:598px"></div>
  <article class="abs col" style="left:634px">
    <h2>Who We Are!</h2><h3>design on your choice</h3>
    <div class="pic"><div role="img" aria-label="Home bar counter with stools" style="background:linear-gradient(135deg,#7a4a24,#c39a63 50%,#6a3c1c)"></div></div>
    <p>Aliquam eleifend lacus ac tellus volutpat porttitor. Suspendisse imperdiet tortor ut tortor bibendum pulvinar...</p>
  </article>
</section>

<div class="abs rule" style="top:920px"></div>

<section>
  <h2 class="abs section-title" style="left:101px;top:936px">Quick Enquiry</h2>
  <div class="abs field" style="top:974px;height:22px;line-height:22px">Your Name</div>
  <div class="abs field" style="top:1004px;height:22px;line-height:22px">Email</div>
  <div class="abs field" style="top:1036px;height:55px;padding-top:6px;line-height:14.5px">Tell Us About Your Project and your Requirment</div>
  <div class="abs submit">Submit</div>
  <div class="abs vline"></div>

  <h2 class="abs section-title" style="left:396px;top:936px">Our Products</h2>
  <div class="abs products"></div>
  <svg class="abs" style="left:364px;top:1013px" width="24" height="42" viewBox="0 0 24 42"><path d="M24 0 A21 21 0 0 0 24 42Z" fill="#444" stroke="#ddd" stroke-width="2"/><path d="M18 13 L10 21 L18 29Z" fill="#fff"/></svg>
  <div class="abs thumb" style="left:396px;width:137px"><div role="img" aria-label="Stainless handrail bracket on glass" style="background:linear-gradient(90deg,#9a9d9f,#d6d8d9 50%,#8c8f91)"></div></div>
  <div class="abs thumb" style="left:542px;width:134px"><div role="img" aria-label="Stainless rod fitting on timber post" style="background:linear-gradient(90deg,#9fb5bb,#c4d2d4 60%,#8b6a44)"></div></div>
  <div class="abs thumb" style="left:685px;width:137px"><div role="img" aria-label="Stainless spigot base" style="background:linear-gradient(90deg,#cfcfcf,#8f8f8f 50%,#e0e0e0)"></div></div>
  <svg class="abs" style="left:830px;top:1013px" width="24" height="42" viewBox="0 0 24 42"><path d="M0 0 A21 21 0 0 1 0 42Z" fill="#444" stroke="#ddd" stroke-width="2"/><path d="M6 13 L14 21 L6 29Z" fill="#fff"/></svg>
</section>

<div class="abs rule" style="top:1128px"></div>

<footer class="abs footer">
  <nav><span>Home</span>~<span>About</span>~<span>Halvard</span>~<span>Products</span>~<span>Download</span>~<span>Contact us</span></nav>
  <p>Copyright © HALVARD. All Rights Reserved.</p>
</footer>
</body>
</html>
```